Australia-Wide Industry Leader Bookkeeping Business Website Design Required

We need a website designed for our 10 year old bookkeeping business, Linden & Crane. Linden & Crane has been servicing the local & interstate communities of Australia, providing first-class BAS & Bookkeeping services with a personal touch unmatched by anyone else in the county.

What began 10 years ago as a small business focusing on family, friends and the local community, it has since grown into a well respected business with 95% of their business based solely on word of mouth and personal referrals from around Australia.

We would like to see designs that incorporate our existing brand/logo. The colours to be used on the website should be colours that work well with our logo. The design should communicate maturity, trust and confidence with a Web 2.0 look and feel.

We have produced mockups of the entire website as well as assets used in the mockups. Please reference the attached files. The mockups are an example of all the design elements that we want on each page. Designers are encouraged to use the mockups as a guideline only and for designers to use their own creativity.
Updates

This message is for new graphic designers who are considering commencing work on this project. Thank you for expressing an interest in our project. We would like to inform you that this project is close to completion as we have a number designs under very serious consideration.

We are currently in a position where we are disinterested providing feedback to improve on new designs submitted. We will provide feedback to improve new designs only if the submitted designs are very close to what we want for our website, and will only require 1 or 2 revision rounds to refine before the project completion date we will not work with designers to refine their newly submitted designs.

We feel that it is important for all designers to know the above information as we feel that your time and effort may be better spent working on another project.

Thank you for your understanding.

A big thank you for all the designs submitted. We are now in the process of selecting a design. Please be patient during this process. Thank you.

Target Market(s)

Busy Business Owners

Industry/Entity Type

Small Business

Requirements
Must have
• We require a rectangular "slide show" type feature to serve as a "teaser" to arouse the emotions of our website visitors. Each slide asks a specific question. The questions are:

- Is your paperwork in a mess?
- Do you need to get organised for the end of financial year?
- Are you sick & tired of endless amounts of paperwork & BASs?
- Do you feel frustrated & annoyed because you know your books need to be done?
- Do you lack the time & patience to get your paperwork done?
- Do you wish you had more time to do the things you enjoy doing?
- Contact Linden & Crane today and we will transform your chaos into order.

Underneath the slide show will be a button to "Call Linden & Crane Now - 03 7482 9163".

```html
<!DOCTYPE html>
<html lang="en">
<head>
<meta charset="utf-8">
<title>Linden &amp; Crane – Bookkeeping</title>
<link href="https://fonts.googleapis.com/css2?family=Ubuntu:wght@400;500;700&family=Ubuntu+Condensed&display=swap" rel="stylesheet">
<style>
:root{
  --red:#9b1111;
  --dark:#2b2b2b;
  --text:#333;
  --muted:#555;
  --grey-band:#f1f1f1;
  --nav-top:#7a7a7a;
  --nav-bot:#3e3e3e;
  --tick:#7cbf2a;
  --blue-top:#39a9f2;
  --blue-bot:#0e7fd6;
  --line:#cfcfcf;
}
*{box-sizing:border-box;margin:0;padding:0}
html,body{width:760px;height:1200px;overflow:hidden;background:#fff}
body{font-family:"Ubuntu",sans-serif;color:var(--text);position:relative;border-top:3px solid var(--dark)}
.abs{position:absolute}
.brand{left:235px;top:11px;width:290px;height:57px;border:2px solid var(--dark);display:flex;align-items:center;justify-content:center;gap:10px}
.brand-square{width:16px;height:16px;background:var(--red)}
.brand-name{font-family:"Ubuntu",sans-serif;font-weight:500;font-size:30px;color:var(--red)}
.nav{left:14px;top:79px;width:726px;height:38px;border-radius:3px;background:linear-gradient(#8a8a8a,var(--nav-bot));display:flex;align-items:center;padding-left:80px;font-family:"Ubuntu Condensed",sans-serif;font-size:13px;color:#fff}
.nav a{color:#fff;text-decoration:none;padding:0 10px;border-left:1px solid #999;line-height:14px}
.nav a.first{border:none}
.nav a.active{background:var(--red);height:38px;line-height:38px;padding:0 11px;margin-right:3px;border:none}
.banner{left:14px;top:133px;width:726px;height:68px;background:linear-gradient(#fff,#ececec);border:1px solid #e4e4e4;color:var(--red);font-size:12.4px;line-height:18.5px;text-align:center;padding-top:15px}
h2{font-weight:500;font-size:12.5px;color:var(--red)}
.copy{font-size:7.6px;line-height:13.4px;color:var(--muted);text-align:justify}
.divider{height:0;border-top:1px dotted var(--line)}
.ticks{list-style:none;font-size:8.8px;color:var(--dark)}
.ticks li{display:flex;align-items:center;gap:7px}
.ticks svg{flex:none}
.subs{list-style:none;font-size:8.6px;color:var(--muted);margin-left:30px}
.subs li{display:flex;align-items:center;gap:8px;height:15px}
.subs li::before{content:"";border-left:4px solid var(--tick);border-top:3px solid transparent;border-bottom:3px solid transparent}
.photo{left:523px;top:225px;width:214px;height:203px;background:#ececec}
.photo-img{height:98px;background:linear-gradient(135deg,#e9edf2,#b9c2cc 60,#6f7d8c)}
.question{font-size:12px;line-height:20px;color:#444;text-align:center;padding-top:33px}
.call{left:523px;top:467px;width:214px;height:49px;border-radius:7px;background:linear-gradient(var(--blue-top),var(--blue-bot));color:#fff;display:flex;align-items:center;gap:14px;padding-left:24px}
.call-lines{text-align:center;line-height:16px}
.call-lines b{display:block;font-weight:400;font-size:17px;letter-spacing:.5px}
.call-lines span{font-size:13px}
.map{left:535px;top:607px;width:205px;height:172px;background:linear-gradient(#e3e3e3,#c9c9c9);border-radius:40px 60px 30px 70px}
.partners{left:22px;top:1007px;width:726px;height:126px;background:linear-gradient(#fff,#ededed);display:flex;align-items:center;justify-content:space-around;padding:0 25px}
.badge{background:#cfcfcf}
.footer-line{left:20px;top:1152px;width:726px;height:3px;background:#111}
.follow{left:22px;top:1164px;font-size:9px;display:flex;align-items:center;gap:6px}
.social{width:18px;height:18px;border-radius:3px}
.copyright{right:15px;top:1169px;font-size:9px}
</style>
</head>
<body>

<div class="abs brand"><span class="brand-square"></span><span class="brand-name">Linden &amp; Crane</span></div>

<nav class="abs nav">
  <a class="active" href="#">Home</a>
  <a class="first" href="#">About Us</a>
  <a href="#">Services</a>
  <a href="#">Testimonials</a>
  <a href="#">Articles</a>
  <a href="#">Endorsements</a>
  <a href="#">Links</a>
  <a href="#">Contact Us</a>
</nav>

<div class="abs banner">For nearly 10 years Linden &amp; Crane has been servicing the local &amp; interstate communities of Australia, Providing first-class<br>BAS &amp; Bookkeeping services with a personal touch unmatched by anyone else in the county.</div>

<section class="abs" style="left:18px;top:223px;width:472px">
  <h2>Welcome to Linden &amp; Crane Website</h2>
  <p class="copy" style="margin-top:6px">Brightpath Web Studio is a web service company, offering a wide range of services which range from designing and development, that is covering almost all the fields in the best possible way. To be the best we know what and how to present beautifully the working of the client's need and their advantages be highlighted. We act in accordance with the Industry certified processes to deliver the best to our clients all over the world.</p>
  <p class="copy" style="margin-top:13px">Thus, Wanna get ahead in the competition with other websites.... Brightpath Web Studio provide you with an attractive and most convincing website to enhance your marketing goals.<br>The only way to success is through the right path and that's what we provide you. None of the other companies has the result we do. So stick to the best that's how you will be the best don't opt for the second best. We partner hundreds of organization to enhance their business, marketing and profit goals.</p>
</section>

<div class="abs divider" style="left:20px;top:408px;width:470px"></div>

<section class="abs" style="left:18px;top:423px;width:472px">
  <h2>To Summarise</h2>
  <div style="display:flex;margin-top:10px">
    <ul class="ticks" style="width:233px">
      <li style="height:18.6px"><svg width="13" height="13" viewBox="0 0 13 13"><circle cx="6.5" cy="6.5" r="6.5" fill="#7cbf2a"/><path d="M3.5 6.8l2 2 4-4.3" stroke="#fff" stroke-width="1.6" fill="none"/></svg>FREE intial consulation</li>
      <li style="height:18.6px"><svg width="13" height="13" viewBox="0 0 13 13"><circle cx="6.5" cy="6.5" r="6.5" fill="#7cbf2a"/><path d="M3.5 6.8l2 2 4-4.3" stroke="#fff" stroke-width="1.6" fill="none"/></svg>Registered BAS Agent #48215-113</li>
      <li style="height:18.6px"><svg width="13" height="13" viewBox="0 0 13 13"><circle cx="6.5" cy="6.5" r="6.5" fill="#7cbf2a"/><path d="M3.5 6.8l2 2 4-4.3" stroke="#fff" stroke-width="1.6" fill="none"/></svg>Bookkeeping</li>
      <li style="height:18.6px"><svg width="13" height="13" viewBox="0 0 13 13"><circle cx="6.5" cy="6.5" r="6.5" fill="#7cbf2a"/><path d="M3.5 6.8l2 2 4-4.3" stroke="#fff" stroke-width="1.6" fill="none"/></svg>BAS Preparation &amp; Logdgement</li>
      <li style="height:18.6px"><svg width="13" height="13" viewBox="0 0 13 13"><circle cx="6.5" cy="6.5" r="6.5" fill="#7cbf2a"/><path d="M3.5 6.8l2 2 4-4.3" stroke="#fff" stroke-width="1.6" fill="none"/></svg>Payroll</li>
      <li style="height:18.6px"><svg width="13" height="13" viewBox="0 0 13 13"><circle cx="6.5" cy="6.5" r="6.5" fill="#7cbf2a"/><path d="M3.5 6.8l2 2 4-4.3" stroke="#fff" stroke-width="1.6" fill="none"/></svg>IAS Preperation &amp; Logdgement</li>
    </ul>
    <ul class="ticks">
      <li style="height:18.6px"><svg width="13" height="13" viewBox="0 0 13 13"><circle cx="6.5" cy="6.5" r="6.5" fill="#7cbf2a"/><path d="M3.5 6.8l2 2 4-4.3" stroke="#fff" stroke-width="1.6" fill="none"/></svg>Superannuation &amp; Workcover</li>
      <li style="height:18.6px"><svg width="13" height="13" viewBox="0 0 13 13"><circle cx="6.5" cy="6.5" r="6.5" fill="#7cbf2a"/><path d="M3.5 6.8l2 2 4-4.3" stroke="#fff" stroke-width="1.6" fill="none"/></svg>Margin Scheme</li>
      <li style="height:18.6px"><svg width="13" height="13" viewBox="0 0 13 13"><circle cx="6.5" cy="6.5" r="6.5" fill="#7cbf2a"/><path d="M3.5 6.8l2 2 4-4.3" stroke="#fff" stroke-width="1.6" fill="none"/></svg>Fuel Tax Credits</li>
      <li style="height:18.6px"><svg width="13" height="13" viewBox="0 0 13 13"><circle cx="6.5" cy="6.5" r="6.5" fill="#7cbf2a"/><path d="M3.5 6.8l2 2 4-4.3" stroke="#fff" stroke-width="1.6" fill="none"/></svg>Offsite &amp; onsite bookkeeping</li>
      <li style="height:18.6px"><svg width="13" height="13" viewBox="0 0 13 13"><circle cx="6.5" cy="6.5" r="6.5" fill="#7cbf2a"/><path d="M3.5 6.8l2 2 4-4.3" stroke="#fff" stroke-width="1.6" fill="none"/></svg>Ledgerly Software &amp; Training</li>
      <li style="height:18.6px"><svg width="13" height="13" viewBox="0 0 13 13"><circle cx="6.5" cy="6.5" r="6.5" fill="#7cbf2a"/><path d="M3.5 6.8l2 2 4-4.3" stroke="#fff" stroke-width="1.6" fill="none"/></svg>Australiawide</li>
    </ul>
  </div>
</section>

<div class="abs divider" style="left:20px;top:587px;width:470px"></div>

<section class="abs" style="left:18px;top:607px;width:472px">
  <h2>What makes Linden &amp; Crane diffrent from other Bookkeepers</h2>
  <ul class="ticks" style="margin-top:12px;margin-left:9px">
    <li style="height:19.4px"><svg width="13" height="13" viewBox="0 0 13 13"><circle cx="6.5" cy="6.5" r="6.5" fill="#7cbf2a"/><path d="M3.5 6.8l2 2 4-4.3" stroke="#fff" stroke-width="1.6" fill="none"/></svg>We guarantee the quality of our work.</li>
    <li style="height:19.4px"><svg width="13" height="13" viewBox="0 0 13 13"><circle cx="6.5" cy="6.5" r="6.5" fill="#7cbf2a"/><path d="M3.5 6.8l2 2 4-4.3" stroke="#fff" stroke-width="1.6" fill="none"/></svg>We have over 35 years of experience</li>
    <li style="height:19.4px"><svg width="13" height="13" viewBox="0 0 13 13"><circle cx="6.5" cy="6.5" r="6.5" fill="#7cbf2a"/><path d="M3.5 6.8l2 2 4-4.3" stroke="#fff" stroke-width="1.6" fill="none"/></svg>We have owned &amp; operated businesses for 35 years</li>
    <li style="height:19.4px"><svg width="13" height="13" viewBox="0 0 13 13"><circle cx="6.5" cy="6.5" r="6.5" fill="#7cbf2a"/><path d="M3.5 6.8l2 2 4-4.3" stroke="#fff" stroke-width="1.6" fill="none"/></svg>The Linden &amp; Crane team are investor &amp; traders</li>
    <li style="height:19.4px"><svg width="13" height="13" viewBox="0 0 13 13"><circle cx="6.5" cy="6.5" r="6.5" fill="#7cbf2a"/><path d="M3.5 6.8l2 2 4-4.3" stroke="#fff" stroke-width="1.6" fill="none"/></svg>Extensive business network for your benefit</li>
    <li style="height:19.4px"><svg width="13" height="13" viewBox="0 0 13 13"><circle cx="6.5" cy="6.5" r="6.5" fill="#7cbf2a"/><path d="M3.5 6.8l2 2 4-4.3" stroke="#fff" stroke-width="1.6" fill="none"/></svg>Backed by a team of Accountants</li>
    <li style="align-items:flex-start;padding-top:3px"><svg width="13" height="13" viewBox="0 0 13 13"><circle cx="6.5" cy="6.5" r="6.5" fill="#7cbf2a"/><path d="M3.5 6.8l2 2 4-4.3" stroke="#fff" stroke-width="1.6" fill="none"/></svg><span style="line-height:13px">We Work with a team of elite accountants &amp; wealth creation professionals who coach us monthly in<br>the following:</span></li>
  </ul>
  <ul class="subs" style="margin-top:6px">
    <li>Assest Protection</li>
    <li>Superannuation &amp; Self Managed Supernnuation Funds</li>
    <li>Property Investing</li>
    <li>Tax Strategies tax structure &amp; best tax savigns</li>
  </ul>
  <ul class="ticks" style="margin-top:6px;margin-left:9px">
    <li style="height:18px"><svg width="13" height="13" viewBox="0 0 13 13"><circle cx="6.5" cy="6.5" r="6.5" fill="#7cbf2a"/><path d="M3.5 6.8l2 2 4-4.3" stroke="#fff" stroke-width="1.6" fill="none"/></svg>We understand just how important it is to help lead &amp; guide our clients for making profits to:</li>
  </ul>
  <ul class="subs" style="margin-top:2px">
    <li style="height:18.6px">Maximising Profits</li>
    <li style="height:18.6px">Wealth Creation</li>
    <li style="height:18.6px">Tax minimisation</li>
    <li style="height:18.6px">Assest Protection</li>
  </ul>
  <p style="font-size:9px;font-weight:500;color:#111;margin:10px 0 0 29px">This is something that other bookkeepers just don't do!</p>
</section>

<div class="abs" style="left:510px;top:225px;height:770px;border-left:1px solid #eee"></div>

<aside class="abs photo">
  <div class="photo-img" role="img" aria-label="Close-up of reading glasses and a pen resting on a printed ledger"></div>
  <p class="question">Do you feel frustrated &amp;<br>annoyed because you know<br>your books need to be done?</p>
</aside>

<a class="abs call" href="#" style="text-decoration:none" aria-label="Call Linden &amp; Crane Now - 03 7482 9163">
  <svg width="28" height="28" viewBox="0 0 24 24"><path fill="#fff" d="M6.6 10.8c1.4 2.8 3.8 5.1 6.6 6.6l2.2-2.2c.3-.3.7-.4 1-.2 1.1.4 2.3.6 3.6.6.6 0 1 .4 1 1V20c0 .6-.4 1-1 1C10.6 21 3 13.4 3 4c0-.6.4-1 1-1h3.5c.6 0 1 .4 1 1 0 1.3.2 2.5.6 3.6.1.3 0 .7-.2 1L6.6 10.8z"/></svg>
  <span class="call-lines"><b>CALL US NOW</b><span>03 7482 9163</span></span>
</a>

<section class="abs" style="left:528px;top:537px;width:200px">
  <h2 style="font-size:10px">Servicing All of Australia</h2>
  <p class="copy" style="margin-top:6px;font-size:7.8px;color:#333">To be the best we know what and how to present beautifully the working of the client's need and their advantages be highlighted.</p>
</section>

<div class="abs map" role="img" aria-label="Map of Australia showing state borders and service locations"></div>

<section class="abs" style="left:523px;top:802px;width:220px">
  <h2 style="font-size:10.2px">Qualifications, Memberships and Partnerships</h2>
  <ul class="ticks" style="margin-top:10px;margin-left:5px;font-size:8.6px;color:#444">
    <li style="height:18.6px"><svg width="13" height="13" viewBox="0 0 13 13"><circle cx="6.5" cy="6.5" r="6.5" fill="#7cbf2a"/><path d="M3.5 6.8l2 2 4-4.3" stroke="#fff" stroke-width="1.6" fill="none"/></svg>Registered National Tax BAS Agent</li>
    <li style="height:18.6px"><svg width="13" height="13" viewBox="0 0 13 13"><circle cx="6.5" cy="6.5" r="6.5" fill="#7cbf2a"/><path d="M3.5 6.8l2 2 4-4.3" stroke="#fff" stroke-width="1.6" fill="none"/></svg>Certificate IV Financial Services</li>
    <li style="height:18.6px"><svg width="13" height="13" viewBox="0 0 13 13"><circle cx="6.5" cy="6.5" r="6.5" fill="#7cbf2a"/><path d="M3.5 6.8l2 2 4-4.3" stroke="#fff" stroke-width="1.6" fill="none"/></svg>Certificate III Financial Services</li>
    <li style="height:18.6px"><svg width="13" height="13" viewBox="0 0 13 13"><circle cx="6.5" cy="6.5" r="6.5" fill="#7cbf2a"/><path d="M3.5 6.8l2 2 4-4.3" stroke="#fff" stroke-width="1.6" fill="none"/></svg>Member of Institute of Chartered</li>
    <li style="height:18.6px"><svg width="13" height="13" viewBox="0 0 13 13"><circle cx="6.5" cy="6.5" r="6.5" fill="#7cbf2a"/><path d="M3.5 6.8l2 2 4-4.3" stroke="#fff" stroke-width="1.6" fill="none"/></svg>Bookkeepres</li>
    <li style="height:18.6px"><svg width="13" height="13" viewBox="0 0 13 13"><circle cx="6.5" cy="6.5" r="6.5" fill="#7cbf2a"/><path d="M3.5 6.8l2 2 4-4.3" stroke="#fff" stroke-width="1.6" fill="none"/></svg>Platinum Member of Southern Bookkeepers Guild</li>
    <li style="height:18.6px"><svg width="13" height="13" viewBox="0 0 13 13"><circle cx="6.5" cy="6.5" r="6.5" fill="#7cbf2a"/><path d="M3.5 6.8l2 2 4-4.3" stroke="#fff" stroke-width="1.6" fill="none"/></svg>Tallyworks Professional Partner</li>
  </ul>
</section>

<div class="abs partners">
  <div class="badge" style="width:58px;height:97px"></div>
  <div class="badge" style="width:90px;height:97px;border-radius:6px"></div>
  <div class="badge" style="width:108px;height:84px"></div>
  <div class="badge" style="width:40px;height:72px"></div>
  <div class="badge" style="width:186px;height:44px"></div>
</div>

<div class="abs footer-line"></div>
<div class="abs follow">Follow us:
  <span class="social" style="background:#3b5a9a;margin-left:4px"></span>
  <span class="social" style="background:#3aa8e0"></span>
</div>
<div class="abs copyright">Copyright © 2012, Linden &amp; Crane. All Right Reserved</div>

</body>
</html>
```